ashby paving works

Needs to have phone number 0412885107 and email marklowry@pavemail.com.au.
ABN 27613048852
name mark lowry

For all your concreting solutions
Excavation
Exposed & colour concrete
House & shed slabs
Driveways
Landing & steps

Contact Information for Business Card

ph 0412885107
email marklowry@pavemail.com.au.
ABN 27613048852
name mark lowry

```html
<!DOCTYPE html>
<html lang="en">
<head>
<meta charset="utf-8">
<title>Ashby Paving Works – Business Card</title>
<link href="https://fonts.googleapis.com/css2?family=Arimo:wght@400;700&family=Montserrat:wght@500;600;700&display=swap" rel="stylesheet">
<style>
  :root {
    --bg: #f2f3f2;
    --paper: #ffffff;
    --orange: #f26f36;
    --orange-soft: rgba(242, 111, 54, 0.85);
    --orange-fade: rgba(242, 111, 54, 0);
    --gold: #f5a623;
    --band-grey: #6d6d6d;
    --charcoal: #3a3a3f;
    --ink: #111111;
    --rule: #555a62;
    --white: #ffffff;
  }
  * { margin: 0; padding: 0; box-sizing: border-box; }
  html, body { width: 1200px; height: 1200px; overflow: hidden; }
  body { background: var(--bg); position: relative; font-family: "Arimo", Arial, sans-serif; }

  .card {
    position: absolute;
    left: 270px;
    width: 660px;
    height: 376px;
    background: var(--paper);
    overflow: hidden;
    box-shadow: 0 14px 30px rgba(0,0,0,0.18);
  }
  .card--front { top: 155px; }
  .card--back { top: 668px; }

  /* Front */
  .front-band {
    position: absolute; left: 0; top: 292px;
    width: 660px; height: 50px;
    background: var(--band-grey);
  }
  .front-accent {
    position: absolute; top: 100px; width: 200px; height: 260px;
  }
  .front-accent--left {
    left: 0;
    background: linear-gradient(to right, var(--orange-soft), var(--orange-fade));
  }
  .front-accent--right {
    right: 0;
    background: linear-gradient(to left, var(--orange-soft), var(--orange-fade));
  }
  .front-brand {
    position: absolute;
    left: 0; right: 0; top: 92px;
    display: flex; flex-direction: column; align-items: center;
  }
  .front-brand__mark {
    width: 56px; height: 56px;
    background: var(--orange);
    margin-bottom: 60px;
  }
  .front-brand__name {
    font-family: "Montserrat", sans-serif;
    font-weight: 600;
    font-size: 22px;
    letter-spacing: 0.5px;
    color: var(--orange);
  }

  /* Back */
  .back-panel {
    position: absolute; left: 291px; top: 0;
    width: 369px; height: 376px;
    background: var(--charcoal);
  }
  .back-accent {
    position: absolute; left: 278px; top: 0;
    width: 170px; height: 376px;
    background: linear-gradient(to right, var(--orange-soft), var(--orange-fade));
  }
  .back-brand {
    position: absolute; left: 14px; top: 14px;
    display: flex; align-items: center; gap: 8px;
  }
  .back-brand__mark { width: 28px; height: 28px; background: var(--orange); }
  .back-brand__divider { width: 1px; height: 44px; background: var(--orange); }
  .back-brand__text {
    font-family: "Montserrat", sans-serif; font-weight: 600;
    color: var(--orange); line-height: 1.15;
  }
  .back-brand__name { font-size: 9.5px; }
  .back-brand__phone { font-size: 7px; letter-spacing: 1.2px; text-align: center; }

  .person {
    position: absolute; left: 48px; top: 166px; width: 212px;
  }
  .person__name {
    font-size: 30px; color: var(--ink); letter-spacing: -0.5px;
    white-space: nowrap; line-height: 1;
  }
  .person__first { font-weight: 700; }
  .person__last { font-weight: 400; }
  .person__company {
    margin-top: 6px; padding-left: 44px;
    font-family: "Montserrat", sans-serif; font-weight: 600;
    font-size: 12.5px; color: var(--orange); white-space: nowrap;
  }
  .person__rule {
    position: relative; margin-top: 2px; height: 2px; width: 208px; background: var(--rule);
  }
  .person__rule::before {
    content: ""; position: absolute; left: 0; top: 0;
    width: 34px; height: 3px; background: var(--gold);
  }

  .contact-list {
    position: absolute; left: 330px; top: 148px;
    list-style: none; color: var(--white); font-size: 17px;
  }
  .contact-list__item {
    display: flex; align-items: center; gap: 18px;
    height: 30px;
  }
  .contact-list__icon { width: 16px; height: 16px; flex: none; fill: var(--white); }
</style>
</head>
<body>

  <section class="card card--front" aria-label="Business card front">
    <div class="front-band"></div>
    <div class="front-accent front-accent--left" role="img" aria-label="Orange diagonal ribbon decoration"></div>
    <div class="front-accent front-accent--right" role="img" aria-label="Orange diagonal ribbon decoration"></div>
    <div class="front-brand">
      <div class="front-brand__mark"></div>
      <div class="front-brand__name">ASHBY PAVING WORKS</div>
    </div>
  </section>

  <section class="card card--back" aria-label="Business card back">
    <div class="back-panel"></div>
    <div class="back-accent" role="img" aria-label="Orange chevron ribbon decoration"></div>

    <div class="back-brand">
      <div class="back-brand__mark"></div>
      <div class="back-brand__divider"></div>
      <div class="back-brand__text">
        <div class="back-brand__name">ASHBY PAVING WORKS</div>
        <div class="back-brand__phone">0412885107</div>
      </div>
    </div>

    <div class="person">
      <div class="person__name"><span class="person__first">MARK</span> <span class="person__last">LOWRY</span></div>
      <div class="person__company">ASHBY PAVING WORKS</div>
      <div class="person__rule"></div>
    </div>

    <ul class="contact-list">
      <li class="contact-list__item">
        <svg class="contact-list__icon" viewBox="0 0 24 24" aria-hidden="true"><path d="M6.6 10.8a15.2 15.2 0 0 0 6.6 6.6l2.2-2.2a1 1 0 0 1 1-.25 11.4 11.4 0 0 0 3.6.57 1 1 0 0 1 1 1V20a1 1 0 0 1-1 1A17 17 0 0 1 3 4a1 1 0 0 1 1-1h3.5a1 1 0 0 1 1 1c0 1.25.2 2.45.57 3.57a1 1 0 0 1-.25 1z"/></svg>
        <span>+04 1288 5107</span>
      </li>
      <li class="contact-list__item">
        <svg class="contact-list__icon" viewBox="0 0 24 24" aria-hidden="true"><path d="M2 5h20v14H2z M3.5 6.5 12 13l8.5-6.5" fill="none" stroke="var(--white)" stroke-width="2"/></svg>
        <span>marklowry@pavemail.com.au</span>
      </li>
      <li class="contact-list__item">
        <svg class="contact-list__icon" viewBox="0 0 24 24" aria-hidden="true"><path d="M6 2v18l4.5-4.5 3 7 3-1.3-3-6.9H20z"/></svg>
        <span>ABN 27613048852</span>
      </li>
    </ul>
  </section>

</body>
</html>
```